Quillaven Shampoo

Quillaven shampoo is aimed to be a "novelty" item, with an intriguing mix of ingredients including but not limited to CBD & caffeine. We want a design that has a unique way of portraying "Quillaven". Get creative with this one. We want the designers to get creative and think outside of the box, and maybe even get a little crazy (but not too crazy), because that's what the premise of the shampoo is; out of the box thinking -- "Quillaven". Try to incorporate what you think of when you hear the word Quillaven.

On the front of the bottle is where the main design will be shown. On the back will be the ingredients list, and will have a bit more information. The design should flow well with a darkish-brown bottle, pictured in the attachments called "bottle-size-template".

Avoid simple designs. We want our shampoo to stand out, not stand on the shelves. Get creative. IMPORTANT NOTE: Please do not use / inspire from the attachments called "bottle-size-template", as these are to show you what the bottle looks like, and what the label will look like on the bottle. DO NOT MAKE YOUR DESIGN BASED FROM THOSE ATTACHMENTS!

If you are feeling like a winner, you can even insert the correct ingredients list: Purified water (aqua), pure virgin hemp seed oil, green tea essential oil, green tea extract, aloe vera, ginseng extract, cam-phor essential oil, glycerin(vegetable), borage seed oil, lauryl glucoside, coconut oil, yucca extract, dermochlorella extract(seaweed based), nettle extract, coco glucoside, jojoba oil, awapuhi, soluble natural plant collagen, wheat germ glycerides (gluten free), echinacea extract, licorice root extract, cocoa butter, ivy extract, soy protein non-GMO), ascorbyl tetraisopalmitate (palm based), golden seal extract, behenic acid (natural based) guar gum, ylang ylang extract, sea salt.

```html
<!DOCTYPE html>
<html lang="en">
<head>
<meta charset="utf-8">
<title>Quillaven Hair Shampoo – Label</title>
<link href="https://fonts.googleapis.com/css2?family=Nunito:wght@400;600&family=Source+Sans+3:wght@400;600&display=swap" rel="stylesheet">
<style>
  :root {
    --plum: #9c1f5f;
    --plum-soft: #f4dde8;
    --plum-mid: #ecc9da;
    --ink: #4a4a4a;
    --paper: #ffffff;
  }
  * { margin: 0; padding: 0; box-sizing: border-box; }
  html, body { width: 1200px; height: 568px; overflow: hidden; background: var(--paper); }
  .label {
    position: relative;
    width: 1200px;
    height: 568px;
    background: var(--paper);
    font-family: "Source Sans 3", sans-serif;
    color: var(--ink);
  }
  .edge-art {
    position: absolute;
    top: 6px;
    width: 92px;
    height: 556px;
    background: linear-gradient(180deg, var(--plum-soft), var(--plum-mid));
  }
  .edge-art--left { left: 11px; border-radius: 20px 70px 70px 20px; }
  .edge-art--right { left: 1097px; border-radius: 70px 20px 20px 70px; }

  .intro {
    position: absolute;
    left: 149px; top: 64px; width: 420px;
    font-size: 12.5px; line-height: 16.2px;
    text-align: justify;
  }
  .panel {
    position: absolute;
    border: 2px solid var(--plum);
  }
  .panel__title {
    background: var(--plum);
    color: var(--paper);
    text-align: center;
    font-size: 11.5px;
    font-weight: 600;
    letter-spacing: 2px;
    line-height: 16px;
    text-transform: uppercase;
  }
  .panel__body {
    padding: 5px 6px;
    font-size: 12.5px;
    line-height: 20.5px;
    text-align: justify;
  }
  .panel--ingredients { left: 149px; top: 167px; width: 420px; height: 191px; }
  .panel--direction { left: 149px; top: 366px; width: 320px; height: 93px; }
  .panel--direction .panel__body { text-align: left; line-height: 20px; padding-top: 4px; }

  .code-spot {
    position: absolute;
    background: var(--plum);
    color: var(--paper);
    font-size: 11.5px;
    display: flex; align-items: center; justify-content: center;
  }
  .code-spot--qr { left: 411px; top: 477px; width: 58px; height: 77px; }
  .code-spot--bar { left: 485px; top: 370px; width: 84px; height: 184px; }
  .code-spot--bar span { transform: rotate(-90deg); white-space: nowrap; }

  .brand {
    position: absolute;
    left: 717px; top: 67px; width: 233px; height: 94px;
    border: 2px solid var(--plum);
    text-align: center;
    font-family: "Nunito", sans-serif;
    color: var(--plum);
    padding-top: 8px;
  }
  .brand__name { font-size: 44px; font-weight: 600; line-height: 50px; }
  .brand__type { font-size: 20px; font-weight: 600; line-height: 24px; }

  .hero-art {
    position: absolute;
    left: 766px; top: 214px; width: 134px; height: 188px;
    border-radius: 50% 50% 46% 46% / 55% 55% 45% 45%;
    background: linear-gradient(180deg, var(--plum-soft), var(--plum-mid));
  }

  .claim {
    position: absolute;
    left: 733px; top: 441px; width: 200px;
    text-align: center;
    font-family: "Nunito", sans-serif;
  }
  .claim__main {
    color: var(--plum);
    font-size: 15px;
    line-height: 20px;
    padding-bottom: 4px;
    border-bottom: 1.5px solid var(--plum);
    margin: 0 10px;
  }
  .claim__meta { color: var(--ink); font-size: 14px; line-height: 19px; margin-top: 14px; }
</style>
</head>
<body>
<div class="label">
  <div class="edge-art edge-art--left" role="img" aria-label="Line illustration of the right half of a brain in plum outline"></div>

  <p class="intro">This product is specially made with hemp seed oil, which is know for its nutritional and medicinal properties. This ingredient has been rediscovered as a beauty aid due to its moisturizing and anti-again effects. it is a rich source of essential fatty acids, including omega-3, which helps replenish and lubricates the hair the natural way.</p>

  <section class="panel panel--ingredients">
    <h2 class="panel__title">Ingredients List:</h2>
    <p class="panel__body">Purified water (aqua), pure virgin hemp seed oil, green tea essential oil, green tea extract, aloe vera, ginseng extract, cam-phor essential oil, glycerin (vegetable), borage seed oil, lauryl glucoside, coconut oil, yucca extract, dermochlorella extract (seaweed based), nettle extract, coco glucoside, jojoba oil, awapuhi, soluble natural plant collagen, wheat germ glycerides (gluten free), echinacea extract, licorice root extract, cocoa butter, ivy extract, soy protein non-GMO), ascorbyl tetraisopalmitate (palm based), golden seal extract, behenic acid (natural based) guar gum, ylang ylang extract, sea salt.</p>
  </section>

  <section class="panel panel--direction">
    <h2 class="panel__title">Direction</h2>
    <p class="panel__body">Apply hemp Shampoo to wet hair. Massage into scalp and hair, leaves for 23 minutes. Rinse and repeat if necessary. Recommended for daily use with Hemp Conditioner.</p>
  </section>

  <div class="code-spot code-spot--qr">QR</div>
  <div class="code-spot code-spot--bar"><span>Bar code</span></div>

  <div class="brand">
    <div class="brand__name">quillaven</div>
    <div class="brand__type">Hair Shampoo</div>
  </div>

  <div class="hero-art" role="img" aria-label="Line illustration of a brain seen from above in plum outline"></div>

  <div class="claim">
    <p class="claim__main">Strengthnes Weak Hair</p>
    <p class="claim__meta">For All Hair Types<br>500ml/17.7 fl.oz</p>
  </div>

  <div class="edge-art edge-art--right" role="img" aria-label="Line illustration of the left half of a brain in plum outline"></div>
</div>
</body>
</html>
```